Utility Contractor looking for a new website

Water and wastewater utility contractor looking to create a new website that highlights our various services. We are looking for modern web presence that can be updated with current projects and new services as we grow. We have an existing logo that we would like to incorporate into the overall design of the site
Updates

Hi, Thank you for all the design submissions. I have had some time to review and have eliminated the ones I feel are not what I am looking for. Based on the designs that remain, I am looking for a clean (not to many bold colours), modern look that is not to busy (long scrolling page), Thanks, Dean

Target Market(s)

project managers, strata boards, owners, people who make decisions as to who operates their water/wastewater system

Industry/Entity Type

Utility

Font styles to use
Sans Serif

Requirements
Must have
• A min page that describes the company and what we do, A page for each of our services that outlines the service and the benefits of it. the look must be consistent throughout. additionally each service page should have some images related to the service

```html
<!DOCTYPE html>
<html lang="en">
<head>
<meta charset="utf-8">
<title>Clearbrook Utility Services</title>
<link rel="stylesheet" href="https://fonts.googleapis.com/css2?family=Arimo:wght@400;700&display=swap">
<style>
  :root {
    --text-grey: #8c8c8c;
    --text-light: #9a9a9a;
    --panel: #efefef;
    --panel-border: #e2e2e2;
    --accent-blue: #1ea2da;
    --phone-blue: #8fb6d6;
    --white: #ffffff;
    --social: #b9b9b9;
  }
  * { box-sizing: border-box; margin: 0; padding: 0; }
  html, body { width: 1200px; height: 951px; overflow: hidden; background: var(--white); }
  body { position: relative; font-family: "Arimo", Arial, sans-serif; color: var(--text-grey); }

  .brand { position: absolute; left: 94px; top: 52px; display: flex; align-items: center; gap: 12px; }
  .brand-mark { width: 26px; height: 26px; border-radius: 50%; background: var(--accent-blue); }
  .brand-name { color: var(--text-grey); font-weight: 400; font-size: 27px; line-height: 30px; white-space: nowrap; }

  .phone { position: absolute; left: 546px; top: 50px; display: flex; align-items: center; gap: 8px; font-size: 29px; color: var(--text-grey); }

  .search { position: absolute; left: 829px; top: 45px; width: 277px; height: 44px; background: var(--panel); border-radius: 4px; }
  .search-label { position: absolute; left: 11px; top: 15px; font-size: 14px; color: var(--text-light); }
  .search-field { position: absolute; left: 64px; top: 10px; width: 204px; height: 24px; background: var(--white); border-radius: 3px; }
  .search-field svg { position: absolute; right: 6px; top: 3px; }

  .main-nav { position: absolute; top: 138px; left: 0; }
  .main-nav a { position: absolute; top: 0; height: 35px; background: var(--panel); border-radius: 4px 4px 0 0; color: var(--text-grey); font-size: 14.5px; text-decoration: none; display: flex; align-items: center; justify-content: center; }
  .nav-band { position: absolute; left: 93px; top: 172px; width: 1015px; height: 8px; background: var(--panel); }

  .hero { position: absolute; left: 93px; top: 179px; width: 1015px; height: 411px;
    background: linear-gradient(100deg, #c9bfae 0%, #a69a86 22%, #7f786c 40%, #5d5a55 55%, #3c3a38 68%, #a7acb1 82%, #d0d4d8 100%); overflow: hidden; }
  .hero-title { position: absolute; left: 54px; top: 195px; font-size: 33px; color: var(--white); font-weight: 400; letter-spacing: 0.5px; }
  .hero-caption { position: absolute; left: 37px; top: 241px; width: 582px; height: 111px; background: rgba(70,70,70,0.72); border-radius: 10px; padding: 23px 20px 0 22px; color: var(--white); font-size: 16.5px; line-height: 19.5px; }
  .slider-dots { position: absolute; left: 48px; top: 376px; display: flex; gap: 6px; }
  .slider-dots span { width: 18px; height: 18px; border-radius: 50%; background: var(--accent-blue); }
  .slider-dots span.active { background: var(--white); }

  .section-title { position: absolute; top: 609px; font-size: 20px; font-weight: 400; color: var(--text-grey); }

  .about-image { position: absolute; left: 97px; top: 637px; width: 301px; height: 122px; background: linear-gradient(180deg, #ffffff 0%, #d6e6f3 45%, #4f86c0 80%, #2e5f9e 100%); }
  .about-text { position: absolute; left: 95px; top: 769px; width: 307px; font-size: 10.3px; line-height: 13px; color: var(--text-light); text-align: justify; letter-spacing: -0.1px; }

  .button { position: absolute; top: 822px; height: 33px; background: var(--panel); border: 1px solid var(--panel-border); border-radius: 3px; color: var(--text-grey); font-size: 14px; display: flex; align-items: center; justify-content: center; }

  .project { position: absolute; top: 644px; width: 145px; }
  .project-frame { width: 145px; height: 96px; border: 1px solid #dcdcdc; padding: 3px; background: var(--white); }
  .project-photo { width: 100%; height: 100%; }
  .project-title { margin-top: 8px; font-size: 13.5px; color: var(--text-grey); text-decoration: underline; white-space: nowrap; }
  .project-text { margin-top: 5px; font-size: 9.3px; line-height: 12px; color: var(--text-light); text-align: justify; text-align-last: justify; letter-spacing: -0.1px; }

  .footer-band { position: absolute; left: 93px; top: 882px; width: 1015px; height: 6px; background: var(--panel); }
  .copyright { position: absolute; left: 92px; top: 909px; font-size: 12px; color: var(--text-grey); }
  .social { position: absolute; top: 903px; left: 945px; display: flex; gap: 5px; }
  .social span { width: 37px; height: 37px; background: var(--social); }
</style>
</head>
<body>

<header>
  <div class="brand">
    <span class="brand-mark" aria-hidden="true"></span>
    <span class="brand-name">Clearbrook Utility Services</span>
  </div>

  <div class="phone">
    <svg width="26" height="34" viewBox="0 0 26 34" aria-hidden="true">
      <path d="M7 2 L12 9 L9 13 C10 18 13 23 17 26 L21 23 L25 29 L20 33 C10 30 3 18 2 7 Z" fill="var(--phone-blue)"/>
    </svg>
    <span>(800) - 5550 1470</span>
  </div>

  <div class="search">
    <span class="search-label">Search</span>
    <div class="search-field">
      <svg width="18" height="18" viewBox="0 0 18 18" aria-hidden="true">
        <circle cx="11" cy="7" r="5" fill="none" stroke="#cfcfcf" stroke-width="2"/>
        <line x1="7.5" y1="10.5" x2="2" y2="16" stroke="#cfcfcf" stroke-width="2.5" stroke-linecap="round"/>
      </svg>
    </div>
  </div>

  <nav class="main-nav">
    <a href="#" style="left:536px;width:101px">Home page</a>
    <a href="#" style="left:649px;width:103px">About Us</a>
    <a href="#" style="left:761px;width:103px">Our Services</a>
    <a href="#" style="left:873px;width:102px">Latest News</a>
    <a href="#" style="left:984px;width:103px">Contact Us</a>
  </nav>
  <div class="nav-band"></div>
</header>

<section class="hero" role="img" aria-label="Photo of water flowing over the weir of a circular wastewater clarifier">
  <h1 class="hero-title">OUR MISSION</h1>
  <p class="hero-caption">Sed elementum quis quam at elementum. Nullam vulputate risus sit amet imperdiet consequat. Morbi vestibulum aliquet magna ac semper. Cras vestibulum ante a eleifend mattis.</p>
  <div class="slider-dots"><span class="active"></span><span></span><span></span></div>
</section>

<section class="about">
  <h2 class="section-title" style="left:100px">ABOUT US</h2>
  <div class="about-image" role="img" aria-label="Illustration of a splashing blue water wave"></div>
  <p class="about-text">Cras id dui eget odio scelerisque volutpat et id orci. Nulla sagittis, nulla non lobortis elementun Cras id dui eget odio scelerisque volutpat et id orci. Nulla sagittis, non lobortis elementum</p>
  <a class="button" style="left:329px;width:71px">Details</a>
</section>

<section class="projects">
  <h2 class="section-title" style="left:474px">OUR PROJECTS</h2>

  <article class="project" style="left:474px">
    <div class="project-frame"><div class="project-photo" role="img" aria-label="Photo of a circular clarifier tank with walkway" style="background:linear-gradient(180deg,#c9d7e3 0%,#6d7e88 40%,#2d4a6e 70%,#8a8f90 100%)"></div></div>
    <div class="project-title">Lorem ipsum dolor sit</div>
    <p class="project-text">Cras id dui eget odio scelerisque volutpat et id orci. Nulla sagittis, nulla non lobortis elementun</p>
  </article>

  <article class="project" style="left:637px">
    <div class="project-frame"><div class="project-photo" role="img" aria-label="Photo of a long aeration basin at a treatment plant" style="background:linear-gradient(180deg,#d7dde2 0%,#8a8680 30%,#6b4e46 60%,#8a6a60 100%)"></div></div>
    <div class="project-title">Lorem ipsum dolor sit</div>
    <p class="project-text">Cras id dui eget odio scelerisque volutpat et id orci. Nulla sagittis, nulla non lobortis elementun</p>
  </article>

  <article class="project" style="left:800px">
    <div class="project-frame"><div class="project-photo" role="img" aria-label="Photo of water poured from a jug into a glass" style="background:linear-gradient(135deg,#eef4f8 0%,#c8dbe8 50%,#7fa4c0 100%)"></div></div>
    <div class="project-title">Lorem ipsum dolor sit</div>
    <p class="project-text">Cras id dui eget odio scelerisque volutpat et id orci. Nulla sagittis, nulla non lobortis elementun</p>
  </article>

  <article class="project" style="left:963px">
    <div class="project-frame"><div class="project-photo" role="img" aria-label="Photo of a chrome tap running water against a blue sky" style="background:linear-gradient(180deg,#1f6fb8 0%,#2e8fd4 50%,#7fb9de 100%)"></div></div>
    <div class="project-title">Lorem ipsum dolor sit</div>
    <p class="project-text">Cras id dui eget odio scelerisque volutpat et id orci. Nulla sagittis, nulla non lobortis elementun</p>
  </article>

  <a class="button" style="left:1001px;width:107px">More Projects</a>
</section>

<footer>
  <div class="footer-band"></div>
  <p class="copyright">Copyrights ©2014 Clearbrook Utility Services. All rights Reserved</p>
  <div class="social" aria-label="Social links"><span></span><span></span><span></span><span></span></div>
</footer>

</body>
</html>
```